Modern Lawfirm Business Card Design

We're looking for a business card to incorporate the newly created logo we had made.

Ideally looking for a law firm business card demonstrating, modern, minimalist, strong/bold design.

I'm open to any design honestly, but nothing "flashy".

Target Market(s)

Immigration law, family immigration, humanitarian, general legal

Industry/Entity Type

Law Firm

Contact Information for Business Card

Please use dummy information, name, street address, city, state, phone number, email, website.

Font styles to use
Serif
Sans Serif

Requirements
Must have
• Please use dummy information, name, street address, city, state, phone number, email, website.

```html
<!DOCTYPE html>
<html lang="en">
<head>
<meta charset="utf-8">
<title>Valdora Immigration Law – Business Card</title>
<link rel="stylesheet" href="https://fonts.googleapis.com/css2?family=Open+Sans:wght@400;600;700&display=swap">
<style>
  :root {
    --brand-blue: #1f5d9c;
    --brand-blue-deep: #174a80;
    --card-white: #f7f7f7;
    --text-grey: #555a60;
    --page-bg: #d9dbde;
    --on-blue: #ffffff;
  }
  * { margin: 0; padding: 0; box-sizing: border-box; }
  html, body {
    width: 1200px;
    height: 960px;
    overflow: hidden;
    background: var(--page-bg);
    font-family: "Open Sans", Arial, sans-serif;
  }
  .sheet {
    width: 1200px;
    height: 960px;
    display: flex;
    flex-direction: column;
    align-items: center;
    justify-content: center;
    gap: 40px;
  }
  .card {
    position: relative;
    width: 700px;
    height: 400px;
    box-shadow: 0 6px 18px rgba(0,0,0,0.18);
    overflow: hidden;
  }

  /* Back side */
  .card--back {
    background: linear-gradient(135deg, var(--brand-blue) 0%, var(--brand-blue-deep) 100%);
    display: flex;
    align-items: center;
    justify-content: center;
  }
  .wordmark {
    display: flex;
    flex-direction: column;
    align-items: flex-start;
    font-weight: 700;
    text-transform: uppercase;
    line-height: 1;
  }
  .wordmark__name { font-size: 64px; letter-spacing: 2px; }
  .wordmark__tag { font-size: 17px; letter-spacing: 9px; margin-top: 6px; }
  .card--back .wordmark { color: var(--on-blue); }

  /* Front side */
  .card--front { background: var(--card-white); }
  .card__content {
    position: absolute;
    left: 60px;
    top: 52px;
  }
  .card--front .wordmark { color: var(--brand-blue); }
  .card--front .wordmark__name { font-size: 46px; letter-spacing: 1.5px; }
  .card--front .wordmark__tag { font-size: 12px; letter-spacing: 6.4px; margin-top: 5px; }

  .person { margin-top: 36px; }
  .person__name {
    color: var(--brand-blue);
    font-weight: 700;
    font-size: 21px;
    text-transform: uppercase;
    letter-spacing: 0.5px;
  }
  .person__role { color: var(--text-grey); font-size: 17px; margin-top: 1px; }

  .contact {
    margin-top: 22px;
    color: var(--text-grey);
    font-size: 16px;
    line-height: 1.5;
    font-style: normal;
  }
  .contact__label { color: var(--brand-blue); font-weight: 700; }

  .web-band {
    position: absolute;
    right: 0;
    top: 0;
    width: 66px;
    height: 100%;
    background: var(--brand-blue);
    display: flex;
    align-items: center;
    justify-content: center;
  }
  .web-band__url {
    writing-mode: vertical-rl;
    color: var(--on-blue);
    font-size: 16px;
    letter-spacing: 4px;
  }
</style>
</head>
<body>
  <main class="sheet">
    <section class="card card--back" aria-label="Card back">
      <div class="wordmark">
        <span class="wordmark__name">Valdora</span>
        <span class="wordmark__tag">Immigration Law</span>
      </div>
    </section>

    <section class="card card--front" aria-label="Card front">
      <div class="card__content">
        <div class="wordmark">
          <span class="wordmark__name">Valdora</span>
          <span class="wordmark__tag">Immigration Law</span>
        </div>
        <div class="person">
          <p class="person__name">Mark Ellison</p>
          <p class="person__role">President</p>
        </div>
        <address class="contact">
          4120 Birchwood Drive<br>
          Juneau, Alaska 99801<br>
          <span class="contact__label">Phone :</span> 555 210 4786<br>
          <span class="contact__label">Email :</span> mark@valdora.com
        </address>
      </div>
      <div class="web-band">
        <span class="web-band__url">www.valdora.com</span>
      </div>
    </section>
  </main>
</body>
</html>
```